Binder design for a veterinary clinic

We are seeking a talented designer to create a standout design for ring binders specifically for our veterinary clinic. These binders will be used to organize materials from our Continuing Professional Development (CPD) projects for colleagues and interns. The design should be clean, professional, and align with our brand guidelines. To give you a better understanding of our branding, we’ve included the design of our vehicles as a reference. As additional reference, please visit www.tierpraxolend.at

Target Market(s)

veterinarians

Industry/Entity Type

Veterinary

Font styles to use
Sans Serif

Colors
0054AA
0677BA
7BADD7
CADEEF
E8F1F8
FFC000
F8CF3A
FAE287
FDF2CF
FEFAEE

Requirements
Must have
• Our Logo an a clean design
Should not have
• to much images

```html
<!DOCTYPE html>
<html lang="en">
<head>
<meta charset="utf-8">
<title>CPD Binder Cover – Tierpraxolend</title>
<link rel="stylesheet" href="https://fonts.googleapis.com/css2?family=Ubuntu:wght@400;500;700&family=Roboto:wght@300;500&display=swap">
<style>
  :root {
    --navy: #172b4b;
    --navy-light: #213a5c;
    --gold: #d9a514;
    --white: #ffffff;
    --page: #ffffff;
  }
  * { margin: 0; padding: 0; box-sizing: border-box; }
  html, body { width: 1200px; height: 1000px; overflow: hidden; background: var(--page); }
  .canvas { position: relative; width: 1200px; height: 1000px; }
  .binder-cover {
    position: absolute; left: 40px; top: 215px;
    width: 1120px; height: 569px;
    background: var(--navy);
    box-shadow: 0 2px 6px rgba(0,0,0,0.25);
    overflow: hidden;
  }
  .front-watermark {
    position: absolute; left: 762px; top: 225px;
    width: 422px; height: 422px;
  }
  .front-title {
    position: absolute; left: 663px; top: 91px;
    font-family: "Ubuntu", sans-serif; font-weight: 700;
    font-size: 22.8px; color: var(--gold); white-space: nowrap;
  }
  .spine-title {
    position: absolute; left: 567px; top: 44px;
    transform-origin: 0 0; transform: rotate(90deg);
    font-family: "Ubuntu", sans-serif; font-weight: 700;
    font-size: 14.2px; line-height: 16px; color: var(--gold); white-space: nowrap;
  }
  .back-brand {
    position: absolute; left: 45px; top: 469px;
    display: flex; align-items: center; gap: 10px;
  }
  .brand-dot {
    width: 54px; height: 54px; border-radius: 50%;
    background: var(--white); border: 3px solid var(--gold);
  }
  .brand-name {
    font-family: "Ubuntu", sans-serif; font-weight: 700;
    font-size: 18px; color: var(--white);
  }
  .divider {
    position: absolute; left: 228px; top: 469px;
    width: 1px; height: 54px; background: var(--gold);
  }
  .contact {
    position: absolute; left: 244px; top: 471px;
    font-family: "Roboto", sans-serif; font-weight: 300; font-style: normal;
    font-size: 7.6px; line-height: 9.5px; color: var(--white);
  }
  .contact .company { font-weight: 500; margin-bottom: 2px; }
  .contact .gap { margin-top: 2px; }
  .website {
    position: absolute; left: 382px; top: 512px;
    font-family: "Roboto", sans-serif; font-weight: 300;
    font-size: 9.5px; color: var(--white);
  }
  .spine-brand {
    position: absolute; left: 518px; top: 469px; width: 84px;
    display: flex; flex-direction: column; align-items: center; gap: 4px;
  }
  .spine-brand .brand-dot { width: 34px; height: 34px; border-width: 2px; }
  .spine-brand .brand-name { font-size: 11.5px; }
</style>
</head>
<body>
<main class="canvas">
  <section class="binder-cover" aria-label="Ring binder cover, back, spine and front">
    <svg class="front-watermark" viewBox="0 0 422 422" role="img" aria-label="Large faint clinic emblem watermark on the front cover">
      <circle cx="211" cy="211" r="211" fill="var(--navy-light)"/>
    </svg>

    <h1 class="front-title">Continuing Professional Development</h1>
    <div class="spine-title">Continuing Professional Development</div>

    <div class="back-brand">
      <span class="brand-dot"></span>
      <span class="brand-name">Tierpraxolend</span>
    </div>
    <span class="divider"></span>
    <address class="contact">
      <div class="company">Tierpraxolend LS GmbH &amp; Co KG</div>
      <div>Birkenallee 41B, 1210 Wien</div>
      <div>Österreich</div>
      <div class="gap">+43(0)1 58206</div>
      <div class="gap">info@tierpraxolend.at</div>
    </address>
    <div class="website">www.tierpraxolend.at</div>

    <div class="spine-brand">
      <span class="brand-dot"></span>
      <span class="brand-name">Tierpraxolend</span>
    </div>
  </section>
</main>
</body>
</html>
```